Supplement Rebranding Bottle Design

READ WORD DOCUMENT ATTACHED.
We want to rebrand our current health supplements (see below). We do want it to be modern, vibrant and appealing. Very upscale and elegant as it targets primarily women.
Bottle size: see pictures for bottle size, along with sample bottles that we like; we’re open to any bottle similar to the ones attached.
Current bottles: So ideally, we’d keep the core color on each bottle with a new branding/bottle design. But we're open to your suggestion.

Target Market(s)

mostly women but shouldn't be overly feminine

Requirements
Must have
• see bottle sizes attached

```html
<!DOCTYPE html>
<html lang="en">
<head>
<meta charset="utf-8">
<title>Arden Supplement Range</title>
<link href="https://fonts.googleapis.com/css2?family=Montserrat:wght@400;600;700;800&display=swap" rel="stylesheet">
<style>
  :root {
    --bg: #ffffff;
    --ink: #ffffff;
    --liver: #7a4e96;
    --liver-light: #a889c4;
    --liver-lid: #c2afd6;
    --tummy: #d3283d;
    --tummy-light: #ee6d7b;
    --tummy-lid: #ef9ca6;
    --hormone: #58a744;
    --hormone-light: #8fcc77;
    --hormone-lid: #b2d8a1;
    --sugar: #35aed8;
    --sugar-light: #7fd3f1;
    --sugar-lid: #a9ddef;
  }
  html, body {
    margin: 0;
    width: 1200px;
    height: 600px;
    overflow: hidden;
    background: var(--bg);
    font-family: "Montserrat", sans-serif;
  }
  .range {
    position: relative;
    width: 1200px;
    height: 600px;
  }
  .pack {
    position: absolute;
    width: 236px;
  }
  .pack__lid {
    height: 70px;
    border-radius: 4px 4px 0 0;
  }
  .pack__body {
    position: relative;
    height: 325px;
    border-radius: 0 0 16px 16px;
    color: var(--ink);
    overflow: hidden;
  }
  .brand {
    position: absolute;
    left: 22px;
    bottom: 58px;
    writing-mode: vertical-rl;
    transform: rotate(180deg);
    font-weight: 800;
    font-size: 60px;
    letter-spacing: 0.02em;
    line-height: 1;
  }
  .info {
    position: absolute;
    left: 96px;
    right: 0;
  }
  .info__title {
    margin: 0;
    font-weight: 700;
    font-size: 21px;
    line-height: 1.25;
    letter-spacing: 0.18em;
    white-space: nowrap;
  }
  .info__rule {
    width: 108px;
    height: 1px;
    background: rgba(255,255,255,0.55);
    margin: 8px 0 9px;
  }
  .info__claim {
    margin: 0;
    font-weight: 700;
    font-size: 7px;
    line-height: 1.6;
    letter-spacing: 0.2em;
    text-transform: uppercase;
    white-space: nowrap;
  }
  .count {
    display: flex;
    align-items: center;
    gap: 5px;
    margin-top: 17px;
  }
  .count__num {
    padding: 3px 6px;
    border-radius: 2px;
    font-weight: 600;
    font-size: 10px;
    background: rgba(0,0,0,0.16);
  }
  .count__unit {
    font-size: 7px;
    line-height: 1.3;
    letter-spacing: 0.2em;
  }
  .info__type {
    margin: 6px 0 0;
    font-size: 7px;
    letter-spacing: 0.2em;
  }
  .pack--liver { left: 160px; top: 60px; z-index: 1; }
  .pack--liver .pack__lid { background: linear-gradient(90deg, #dcd0e8, var(--liver-lid) 40%, #9d86b4); }
  .pack--liver .pack__body { background: linear-gradient(90deg, var(--liver-light), var(--liver) 45%, #6d4589); }
  .pack--tummy { left: 372px; top: 92px; z-index: 2; }
  .pack--tummy .pack__lid { background: linear-gradient(90deg, #f8c3c9, var(--tummy-lid) 40%, #cf707c); }
  .pack--tummy .pack__body { background: linear-gradient(90deg, var(--tummy-light), var(--tummy) 45%, #c52337); }
  .pack--hormone { left: 585px; top: 124px; z-index: 3; }
  .pack--hormone .pack__lid { background: linear-gradient(90deg, #d3e9c8, var(--hormone-lid) 40%, #8fb97f); }
  .pack--hormone .pack__body { background: linear-gradient(90deg, var(--hormone-light), var(--hormone) 45%, #50a03e); }
  .pack--sugar { left: 797px; top: 156px; z-index: 4; }
  .pack--sugar .pack__lid { background: linear-gradient(90deg, #cdeefa, var(--sugar-lid) 40%, #86c2d8); }
  .pack--sugar .pack__body { background: linear-gradient(90deg, var(--sugar-light), var(--sugar) 45%, #30a4cf); }
</style>
</head>
<body>
<main class="range">
  <article class="pack pack--liver">
    <div class="pack__lid"></div>
    <div class="pack__body">
      <div class="brand">ARDEN</div>
      <div class="info" style="top:135px">
        <h2 class="info__title">LIVER<br>CARE</h2>
        <div class="info__rule"></div>
        <p class="info__claim">Rejuvenating cleanse<br>&amp; detox formula*</p>
        <div class="count"><span class="count__num">120</span><span class="count__unit">VEGETABLE<br>CAPSULES</span></div>
        <p class="info__type">DIETARY SUPPLEMENT</p>
      </div>
    </div>
  </article>
  <article class="pack pack--tummy">
    <div class="pack__lid"></div>
    <div class="pack__body">
      <div class="brand">ARDEN</div>
      <div class="info" style="top:135px">
        <h2 class="info__title">TUMMY<br>CARE</h2>
        <div class="info__rule"></div>
        <p class="info__claim">Oxygenating<br>colon cleanse*</p>
        <div class="count"><span class="count__num">90</span><span class="count__unit">VEGETABLE<br>CAPSULES</span></div>
        <p class="info__type">DIETARY SUPPLEMENT</p>
      </div>
    </div>
  </article>
  <article class="pack pack--hormone">
    <div class="pack__lid"></div>
    <div class="pack__body">
      <div class="brand">ARDEN</div>
      <div class="info" style="top:135px">
        <h2 class="info__title">HORMONE<br>CARE</h2>
        <div class="info__rule"></div>
        <p class="info__claim">Supports healthy<br>hormone levels*</p>
        <div class="count"><span class="count__num">60</span><span class="count__unit">VEGETABLE<br>CAPSULES</span></div>
        <p class="info__type">DIETARY SUPPLEMENT</p>
      </div>
    </div>
  </article>
  <article class="pack pack--sugar">
    <div class="pack__lid"></div>
    <div class="pack__body">
      <div class="brand">ARDEN</div>
      <div class="info" style="top:115px">
        <h2 class="info__title">BLOOD<br>SUGAR<br>CARE</h2>
        <div class="info__rule"></div>
        <p class="info__claim">Supports healthy<br>blood glucose levels*</p>
        <div class="count"><span class="count__num">60</span><span class="count__unit">VEGETABLE<br>CAPSULES</span></div>
        <p class="info__type">DIETARY SUPPLEMENT</p>
      </div>
    </div>
  </article>
</main>
</body>
</html>
```